Layout for new page on existing website

We have an existing website (www.brightloomworks.org) and need a new page designing to promote a new product.
The new page needs to be consistent with the existing website look and feel (www.brightloomworks.org) but current persistent elements on the standard page design can be moved/removed from the page to accommodate a new layout necessary for getting all the content laid out in a logical user friendly way.
The content required for the page is attached along with a wireframe mock up that may help understand the expectation, however the wireframe was just created to help me work out what was needed on the page and the layout can be different. A key element is the quality of the design of each of the artifacts (e.g. the panel the embedded video needs to go in, icons etc) and a clear display of the information.
Updates
The website that the new page needs to fit into is www.brightloomworks.org, i will also added the company logo to the brief.
Our Corporate Colours
- Green: #A2FF00
- Cream: #FFFF99
- Yellow: #FFE900
- Grey: #534741
Industry/Entity Type
Product
Look and feel
Each slider illustrates characteristics of the customer's brand and the style your logo design should communicate.

```html
<!DOCTYPE html>
<html lang="en">
<head>
<meta charset="utf-8">
<title>Brightloom Works – Course Management and Booking</title>
<link href="https://fonts.googleapis.com/css2?family=Arimo:wght@400;700&display=swap" rel="stylesheet">
<style>
:root{
  --bg:#4b423c;
  --panel:#3b3430;
  --panel-edge:#5e544d;
  --yellow:#ffe900;
  --green:#a2ff00;
  --cream:#ffff99;
  --white:#ffffff;
  --black:#000000;
  --text:#f2f2f2;
}
*{box-sizing:border-box;margin:0;padding:0}
html,body{width:1200px;height:2791px;overflow:hidden}
body{background:var(--bg);font-family:"Arimo",Arial,sans-serif;color:var(--text);position:relative}
.abs{position:absolute}
.home-link{left:52px;top:84px;width:72px;text-align:center;color:var(--white);font-size:15px;font-weight:700}
.home-link svg{display:block;margin:0 auto 8px}
.brand{left:0;width:1200px;top:124px;text-align:center;font-size:52px;font-weight:700;letter-spacing:12px;color:var(--white)}
.brand .dot{display:inline-block;width:40px;height:40px;border-radius:50%;background:var(--green);vertical-align:-4px;margin-right:18px}
.section-title{left:0;width:1200px;text-align:center;color:var(--yellow);font-weight:700;font-size:31px}
.banner{left:50px;top:300px;width:1100px;height:258px;background:var(--white);display:flex;align-items:center;justify-content:center;color:var(--black);font-size:44px;font-weight:700}
.video-frame{left:248px;top:645px;width:707px;height:511px;border-radius:14px;background:linear-gradient(160deg,var(--cream) 0%,var(--yellow) 35%,var(--green) 100%);box-shadow:0 0 0 3px #6a7a10 inset}
.video-screen{position:absolute;left:40px;top:43px;width:627px;height:360px;background:var(--black);border:6px solid #2d2d2d}
.video-mark{position:absolute;left:20px;top:428px;width:58px;height:58px;border-radius:50%;background:var(--white)}
.video-title{position:absolute;left:0;width:100%;top:448px;text-align:center;color:var(--black);font-size:30px;font-weight:700}
.testimonial{left:19px;top:1215px;width:1162px;height:171px;background:var(--panel);border-top:2px solid var(--panel-edge);border-bottom:2px solid var(--panel-edge)}
.quote-mark{position:absolute;top:-30px;font-size:230px;font-weight:700;color:#252120;line-height:1;font-family:Georgia,serif}
.testimonial blockquote{position:absolute;left:145px;top:30px;width:880px;color:var(--yellow);font-size:23px;font-weight:700;line-height:1.3}
.testimonial cite{position:absolute;left:145px;top:125px;color:var(--white);font-size:22px;font-weight:700;font-style:normal}
.block-title{left:19px;color:var(--yellow);font-weight:700;font-size:42px}
.feature{width:530px;padding-left:70px;font-size:16px;line-height:1.3;color:var(--text)}
.feature h3{color:var(--yellow);font-size:18px;font-weight:700;margin-bottom:2px}
.feature .icon{position:absolute;left:0;top:0;width:58px;height:56px;border-radius:12px}
.benefits{left:19px;top:2009px;width:1162px;height:301px;background:var(--panel);border:2px solid var(--panel-edge)}
.benefits h2{position:absolute;left:18px;top:16px;color:var(--yellow);font-size:42px}
.benefits p{position:absolute;left:18px;top:78px;width:1120px;font-size:17px;line-height:1.3;color:var(--white)}
.form-panel{left:170px;top:2418px;width:844px;height:310px;background:var(--panel);border:2px solid var(--panel-edge)}
.form-row{position:absolute;left:38px;width:760px;height:38px}
.form-row label{position:absolute;left:0;top:9px;font-size:19px;color:var(--white)}
.form-row span{position:absolute;left:133px;top:0;width:626px;height:37px;background:var(--white)}
.send{position:absolute;left:673px;top:230px;width:124px;height:38px;border-radius:8px;background:var(--yellow);color:var(--black);font-weight:700;font-size:20px;display:flex;align-items:center;justify-content:center}
</style>
</head>
<body>

<a class="abs home-link">
  <svg width="60" height="54" viewBox="0 0 60 54" aria-hidden="true">
    <circle cx="30" cy="28" r="26" fill="#6b5a2a" opacity=".6"/>
    <path d="M10 28 L30 10 L50 28" fill="none" stroke="#ffe900" stroke-width="5" stroke-linejoin="round"/>
    <path d="M17 26 V44 H26 V34 H34 V44 H43 V26" fill="none" stroke="#ffe900" stroke-width="4"/>
  </svg>
  Home
</a>

<div class="abs brand"><span class="dot"></span>BRIGHTLOOM WORKS</div>

<h1 class="abs section-title" style="top:252px">Course Management and Booking Simplified</h1>

<div class="abs banner">Banner</div>

<h2 class="abs section-title" style="top:594px">Built With Your Own Business in Mind</h2>

<div class="abs video-frame">
  <div class="video-screen"></div>
  <div class="video-mark"></div>
  <div class="video-title">Video Title</div>
</div>

<section class="abs testimonial">
  <span class="quote-mark" style="left:18px">&ldquo;</span>
  <span class="quote-mark" style="right:18px;top:40px">&rdquo;</span>
  <blockquote>&ldquo;A convenient tool that was simple to integrate into our website. It has allowed both the business and our customers an easy way to book courses. In life sometimes simple is good and this is a great example!&rdquo;</blockquote>
  <cite>Dana Prescott, Director @ PeakTrain www.peaktrain.org</cite>
</section>

<h2 class="abs block-title" style="top:1420px">Key Features</h2>

<div class="abs feature" style="left:25px;top:1492px">
  <div class="icon" role="img" aria-label="Life ring icon" style="background:radial-gradient(circle,#4b423c 28%,#e23a2a 30%,#fff 70%)"></div>
  <h3>Available and easy to use 24/7</h3>
  <p>By allowing booking and payment at any time of the day, your attendees will be more likely to commit to your event and with no account setup or password required and no paper forms to fill in and post, booking onto and paying for your courses is easy.</p>
</div>
<div class="abs feature" style="left:25px;top:1655px">
  <div class="icon" role="img" aria-label="Book icon" style="background:linear-gradient(135deg,#f3c04a,#b07a14)"></div>
  <h3>Online Course promotion</h3>
  <p>List your upcoming courses in a clear and simple way so people can easily find and select the course that suits them.</p>
</div>
<div class="abs feature" style="left:25px;top:1768px">
  <div class="icon" role="img" aria-label="Coins icon" style="background:linear-gradient(135deg,#f6d36a,#b8860b)"></div>
  <h3>Online &amp; Offline Payments</h3>
  <p>Take payments online, whilst having the flexibility of managing and adding offline.</p>
</div>
<div class="abs feature" style="left:25px;top:1862px">
  <div class="icon" role="img" aria-label="Envelope icon" style="background:linear-gradient(135deg,#f7dc8a,#d4a53c)"></div>
  <h3>Built in email system</h3>
  <p>Enable quick and easy communication with upcoming course candidates and promotion of additional courses to past candidates payments.</p>
</div>

<div class="abs feature" style="left:645px;top:1486px">
  <div class="icon" role="img" aria-label="Tool icon" style="background:linear-gradient(135deg,#a0785a,#5a3d28)"></div>
  <h3>Customisable look and feel</h3>
  <p>All elements of the booking systems design will fit in with your existing websites style.</p>
</div>
<div class="abs feature" style="left:645px;top:1590px">
  <div class="icon" role="img" aria-label="People icon" style="background:linear-gradient(135deg,#7aa0e0,#c04a3a)"></div>
  <h3>Live course place availability</h3>
  <p>By defining minimum and maximum candidates permitted on a course its easy to prevent overbooking and also prevent courses running that don't have</p>
</div>
<div class="abs feature" style="left:645px;top:1715px">
  <div class="icon" role="img" aria-label="Database icon" style="background:linear-gradient(135deg,#9ad4f0,#2f6f98)"></div>
  <h3>Venue database management</h3>
  <p>Easily add, edit and remove venues from which you operate your courses from.</p>
</div>

<section class="abs benefits">
  <h2>Benefits</h2>
  <p>Live Availability – Availability on course place availability to prevent overbooking Customers can search for Courses and Book Online with immediate confirmation Automated confirmation emails Be available for business 24/7 and take orders anytime! Customers can book when it's most convenient for them – be it early morning, late evening or weekend No fielding phone calls, no wading through paper registrations. Attendees book on your website, there and then No more trips to the bank, take immediate and secure payments online Automated confirmation emails so reducing the time need communicating with candidates Boost course bookings and reduce administrative time and costs Course Admin is Web based meaning you can access your course information from anywhere at any time. System is very intuitive and easy to use. Lighten your workload Upload and manage offline bookings through the admin dashboard Keep your attendees organized all the way up to the course date and beyond.</p>
</section>

<h2 class="abs section-title" style="top:2350px;font-size:40px">Contact Us Now for a free no obligation quote</h2>

<form class="abs form-panel">
  <div class="form-row" style="top:38px"><label>Name:</label><span></span></div>
  <div class="form-row" style="top:88px"><label>Company:</label><span></span></div>
  <div class="form-row" style="top:138px"><label>Email:</label><span></span></div>
  <div class="form-row" style="top:188px"><label>Telephone:</label><span></span></div>
  <div class="send">SEND</div>
</form>

</body>
</html>
```